International IT business needs website revamp.

Velbric Limited would like their current website (www.velbriclimited.example) to be revamped/modernized to reflect up-to-date goods and services. Currently, Velbric is offering a conversational AI workflow platform for both enterprise clients and as a DIY solution for SMBs. This platform is called tmPilot and allows organizations to automate simple and repetitive workflows to drive their operational efficiency. In addition to the solution offering, Velbric Limited also provides professional IT services. With that said, please use www.velbriclimited.example and www.tmpilot.example for reference of current logos and colourways desired. Furthermore, refer to the attached PDF for a general idea of what to include in the site. The final design should be easy to navigate, clear, concise, and emphasize tmPilot as a solution for enterprise clients (while redirecting SMBs to the tmPilot website) looking to automate workflow processes/kickstart their digital transformation journey.
Updates
Coding
Number of Pages Required
5+ page
Font styles to use
Look and feel
Each slider illustrates characteristics of the customer's brand and the style your logo design should communicate.

```html
<!DOCTYPE html>
<html lang="en">
<head>
<meta charset="utf-8">
<title>Velbric Limited — Enterprise Conversational AI</title>
<link href="https://fonts.googleapis.com/css2?family=Montserrat:wght@400;600;700;800&family=Roboto:wght@300;400;500;700&display=swap" rel="stylesheet">
<style>
:root{
  --green:#7bc043;
  --green-dark:#5fa12c;
  --ink:#222629;
  --text:#5d6266;
  --muted:#9aa0a4;
  --line:#e3e6e8;
  --soft:#f3f4f5;
  --footer:#1d2124;
  --footer-deep:#15181a;
  --white:#ffffff;
}
*{box-sizing:border-box;margin:0;padding:0}
html,body{width:1200px;height:4964px;overflow:hidden;background:var(--white)}
body{font-family:"Roboto",sans-serif;color:var(--text);position:relative}
.abs{position:absolute}
.section-title{font-family:"Montserrat",sans-serif;font-weight:800;font-size:34px;color:var(--ink);text-align:center;letter-spacing:.5px}
.section-title .chev{color:var(--green);margin-right:6px}
.btn{display:inline-block;background:var(--green);color:var(--white);font:600 13px "Montserrat",sans-serif;letter-spacing:.5px;padding:11px 26px;text-transform:uppercase}
.btn.tag{clip-path:polygon(0 0,90% 0,100% 50%,90% 100%,0 100%)}
.dots{display:flex;gap:8px}
.dots i{width:10px;height:10px;border-radius:50%;background:#cfd3d6;display:block}
.dots i.on{background:var(--green)}

/* top bar */
.topbar{left:0;top:0;width:1200px;height:24px;background:var(--green);color:var(--white);font-size:12px}
.topbar .social{left:175px;top:6px;display:flex;gap:12px}
.topbar .social i{width:12px;height:12px;background:rgba(255,255,255,.85);border-radius:2px;display:block}
.topbar .contact{right:190px;top:5px;display:flex;gap:40px}
/* nav */
.nav{left:0;top:24px;width:1200px;height:90px;background:var(--white)}
.logo{display:flex;align-items:center;gap:8px;font:800 26px "Montserrat",sans-serif;color:var(--ink);letter-spacing:1px}
.logo .mark{width:24px;height:24px;background:var(--ink)}
.nav .logo{left:90px;top:30px}
.menu{right:90px;top:32px;display:flex;gap:28px;align-items:center;font:600 13px "Montserrat",sans-serif;color:var(--ink)}
.menu .active::before{content:"| ";color:var(--green)}
.menu .btn{padding:7px 14px;font-size:12px}
/* hero */
.hero{left:0;top:114px;width:1200px;height:610px;background:linear-gradient(180deg,#f7f8f8,#eceeef)}
.hero-photo{left:630px;top:0;width:430px;height:600px;background:linear-gradient(160deg,#f1efe9 0%,#d9d4c8 45%,#2c2c2e 75%,#1b1b1c 100%)}
.hero h1{left:180px;top:110px;font:800 52px/1.1 "Montserrat",sans-serif;color:var(--green);z-index:2;white-space:nowrap}
.hero .sub{left:180px;top:200px;font:600 26px/1.35 "Montserrat",sans-serif;color:var(--ink);width:420px;z-index:2}
.hero .btn{left:180px;top:292px;z-index:2}
.hero .dots{left:680px;top:570px}
/* partner strip */
.partners{left:0;top:740px;width:1200px;height:120px;border-bottom:1px solid var(--line)}
.partners .row{left:160px;top:44px;width:880px;display:flex;justify-content:space-between;align-items:center;font:700 22px "Roboto",sans-serif;color:#4a4f53}
.arrow{color:#9aa0a4;font:300 46px/1 "Roboto",sans-serif}
/* about */
.about{left:0;top:880px;width:1200px}
.about h2{position:absolute;top:10px;width:1200px}
.about p{position:absolute;left:180px;top:70px;width:840px;font-size:14px;line-height:1.55;text-align:center}
.more{position:absolute;top:190px;width:1200px;text-align:center;font:500 14px "Roboto",sans-serif;color:var(--green);text-decoration:underline}
/* videos */
.videos-title{left:0;top:1130px;width:1200px;line-height:1.2}
.video-frame{left:344px;top:1248px;width:516px;height:212px;background:linear-gradient(135deg,#e2ecd9,#b9d3a8 50%,#7ea36a)}
.play{left:572px;top:1332px;width:60px;height:44px;background:#e53935;border-radius:10px}
.play::after{content:"";position:absolute;left:23px;top:12px;border-left:18px solid #fff;border-top:10px solid transparent;border-bottom:10px solid transparent}
.round-arrow{width:52px;height:52px;border-radius:50%;background:#c7cbce;color:#fff;font:400 34px/50px "Roboto",sans-serif;text-align:center}
.caption{left:0;top:1494px;width:1200px;text-align:center;font:500 20px "Roboto",sans-serif;color:var(--ink)}
.caption small{display:block;font:400 13px "Roboto",sans-serif;color:var(--text);margin-top:4px}
.thumbs{left:200px;top:1680px;width:700px;display:flex;gap:30px}
.thumbs div{width:128px;height:128px}
.video-dots{left:0;top:1846px;width:1200px;text-align:center;font-size:11px;color:var(--muted)}
/* testimonials */
.testi-band{left:0;top:1900px;width:1200px;height:420px;background:var(--soft);clip-path:polygon(0 10%,100% 0,100% 100%,0 90%)}
.testi-title{left:0;top:1950px;width:1200px}
.quote-name{left:0;top:2010px;width:1200px;text-align:center;font-size:13px;color:var(--ink)}
.stars{left:0;top:2030px;width:1200px;text-align:center;color:#f5b301;font-size:18px;letter-spacing:2px}
.quote{left:180px;top:2070px;width:840px;text-align:center;font-size:14px;line-height:1.55}
.testi-dots{left:580px;top:2215px}
/* services */
.services-title{left:0;top:2320px;width:1200px}
.svc{top:2430px;width:250px;text-align:center}
.svc .icon{width:60px;height:60px;margin:0 auto 16px;display:block}
.svc h3{font:700 16px/1.3 "Montserrat",sans-serif;color:var(--green);text-transform:uppercase;margin-bottom:16px}
.svc p{font-size:13px;line-height:1.55}
.svc.card{top:2390px;width:300px;height:400px;background:var(--white);box-shadow:0 6px 28px rgba(0,0,0,.12);padding:40px 24px}
.svc.card .btn{margin-top:40px}
/* solutions */
.solutions-band{left:0;top:2820px;width:1200px;height:380px;background:linear-gradient(180deg,#fff,#f4f5f6)}
.solutions-title{left:180px;top:2880px}
.solutions-text{left:180px;top:2960px;width:460px;font-size:14px;line-height:1.55}
.solutions-btn{left:180px;top:3130px}
.solutions-photo{left:810px;top:2840px;width:260px;height:360px;background:linear-gradient(170deg,#efe9e0 0%,#d8cfc3 40%,#2a2a2c 72%,#1b1b1c 100%)}
/* green wave */
.omni{left:0;top:3650px;width:1200px;height:700px}
.robot{left:760px;top:3760px;width:400px;height:540px;border-radius:200px 200px 20px 20px;background:radial-gradient(circle at 50% 35%,#f3f6f8,#c7d2da 55%,#8ea1ad)}
/* request */
.request-box{left:360px;top:3380px;width:480px;height:440px;background:var(--white);box-shadow:0 4px 24px rgba(0,0,0,.12);padding:26px 18px}
.request-box h2{text-align:left;margin-bottom:22px}
.fields{display:grid;grid-template-columns:1fr 1fr;gap:10px 24px}
.field label{display:block;font-size:12px;color:var(--muted);margin-bottom:6px}
.field label b{color:#e05a4e}
.field .input{height:36px;border:1px solid #cfd3d6}
.field.wide{grid-column:1/3}
.field .area{height:130px;border:1px solid #cfd3d6;padding:8px;font-size:12px;color:#b6bbbf}
.request-box .btn{margin:16px 0 0 170px;padding:9px 24px;font-size:12px}
/* omni text */
.omni-title{left:175px;top:3990px;font:700 30px "Montserrat",sans-serif;color:var(--white)}
.omni-text{left:175px;top:4048px;width:390px;font-size:14px;line-height:1.5;color:var(--white)}
.omni-btn{left:175px;top:4180px;background:#5a9628}
.product-name{left:490px;top:4226px;display:flex;align-items:center;gap:10px;font:800 40px "Montserrat",sans-serif;color:var(--white)}
.product-name i{width:24px;height:24px;border-radius:50%;background:var(--white);display:block}
/* clients */
.clients-row{left:200px;top:4395px;width:800px;display:flex;justify-content:space-between;align-items:center;font:800 34px "Montserrat",sans-serif;color:#1e4fa0}
/* footer */
.footer{left:0;top:4520px;width:1200px;height:380px;background:var(--footer);color:#c5cacd}
.footer .logo{left:90px;top:60px;color:var(--white)}
.footer .logo .mark{background:var(--white)}
.footer .contact{left:90px;top:120px;font-size:13px;line-height:1.65;width:300px}
.fcol{top:80px;font-size:13px;line-height:2.4}
.fcol h4{font:600 14px "Montserrat",sans-serif;color:var(--green);margin-bottom:6px}
.news .input{width:225px;height:30px;background:var(--white);color:#9aa0a4;font-size:11px;padding:8px;line-height:14px}
.news .btn{margin-top:8px;padding:6px 12px;font-size:11px;line-height:1.2}
.bottombar{left:0;top:4900px;width:1200px;height:64px;background:var(--footer-deep);color:#aab0b4;font-size:12px}
.bottombar .copy{left:90px;top:25px}
.bottombar .social{right:100px;top:24px;display:flex;gap:14px}
.bottombar .social i{width:13px;height:13px;background:#8d9397;border-radius:2px;display:block}
</style>
</head>
<body>

<div class="abs topbar">
  <div class="abs social"><i></i><i></i><i></i></div>
  <div class="abs contact"><span>Email: info@velbriclimited.example</span><span>Phone: (555) 014-2290</span></div>
</div>

<header class="abs nav">
  <div class="abs logo"><span class="mark"></span>VELBRIC</div>
  <nav class="abs menu">
    <span class="active">HOME</span><span>ABOUT</span><span>SERVICES</span><span>SOLUTIONS</span><span>PRODUCTS</span><span class="btn">CONTACT</span>
  </nav>
</header>

<section class="abs hero">
  <div class="abs hero-photo" role="img" aria-label="Smiling businesswoman in a dark blazer holding an open laptop"></div>
  <h1 class="abs">COULD IT BE?</h1>
  <p class="abs sub">Finally, An Enterprise Chatbot Platform That Really Delivers</p>
  <span class="abs btn tag">Explore</span>
  <div class="abs dots"><i class="on"></i><i></i><i></i></div>
</section>

<section class="abs partners">
  <span class="abs arrow" style="left:80px;top:36px">‹</span>
  <div class="abs row"><span>Norvale</span><span>Quenta</span><span style="font-size:15px">Brightfield Systems</span><span>Tallyworks</span><span>Arvo</span></div>
  <span class="abs arrow" style="right:80px;top:36px">›</span>
</section>

<section class="abs about">
  <h2 class="section-title"><span class="chev">›</span>ABOUT US</h2>
  <p>Since 2011, the Velbric team has been providing professional IT services for major Canadian corporations operating in the telecommunications and financial sectors. As such, our team is highly skilled in technology integration, legacy modernization, system architecture design, application development, quality assurance, project management and more. As of 2017, we developed and launched tmPilot, a conversational workflow platform powered by AI and ML, into production. Our vision for tmPilot is to drive true operational economy.</p>
  <a class="more">Read More</a>
</section>

<h2 class="abs section-title videos-title"><span class="chev">›</span>OUR EXCLUSIVE<br>VIDEOS</h2>
<div class="abs video-frame" role="img" aria-label="Video still of a service robot in a green-tinted office"></div>
<div class="abs play"></div>
<div class="abs round-arrow" style="left:214px;top:1380px">‹</div>
<div class="abs round-arrow" style="left:890px;top:1380px">›</div>
<div class="abs caption">Robot for more information on how we can assist you through<small>your lit contact us at info@velbriclimited.example for a personal demo</small></div>
<div class="abs thumbs">
  <div role="img" aria-label="Video thumbnail: robot at a desk" style="background:linear-gradient(135deg,#dcdfe1,#6d7479)"></div>
  <div role="img" aria-label="Video thumbnail: robotic arm" style="background:linear-gradient(135deg,#cfe0ea,#7d9bb0)"></div>
  <div role="img" aria-label="Video thumbnail: laboratory automation" style="background:linear-gradient(135deg,#e4ecf0,#9fb5c2)"></div>
  <div role="img" aria-label="Video thumbnail: blue data network" style="background:linear-gradient(135deg,#2f6fb2,#12365e)"></div>
  <div role="img" aria-label="Video thumbnail: humanoid robot" style="background:linear-gradient(135deg,#e8ecee,#8f9aa1)"></div>
</div>
<div class="abs round-arrow" style="left:920px;top:1722px;width:44px;height:44px;line-height:42px;font-size:28px">›</div>
<div class="abs video-dots">● 1 ● 2 ● 3 ● 4 ● 5</div>

<div class="abs testi-band"></div>
<h2 class="abs section-title testi-title"><span class="chev">›</span>TESTIMONIALS</h2>
<div class="abs quote-name">Civic Travel Office</div>
<div class="abs stars">★★★★★</div>
<p class="abs quote">"Naturally, the Civic Travel Office website receives thousands of visitors a day. As a result, we noticed the need to automate simple and repetitive questions to provide quick, on-demand assistance while maximizing our human production to without compromising costs. Thus, we enlisted Velbric Limited and their tmPilot solution to accomplish the task. Since launching the assistant in Q4, 2018, we have achieved over 70% of inquiries being automatically answered successfully!"</p>
<div class="abs dots testi-dots"><i class="on"></i><i></i><i></i></div>

<h2 class="abs section-title services-title"><span class="chev">›</span>OUR SERVICES</h2>
<div class="abs svc" style="left:170px">
  <svg class="icon" viewBox="0 0 60 60" fill="none" stroke="#222629" stroke-width="2"><rect x="12" y="8" width="36" height="46" rx="2"/><path d="M20 20h20M20 28h20M20 36h14"/><circle cx="44" cy="44" r="8" fill="#fff"/></svg>
  <h3>Contract<br>Staffing</h3>
  <p>At Velbric, our staff are readily available to deliver experienced and knowledgeable assistance to fill immediate or temporary needs for a diverse range of technologies and positions.</p>
</div>
<div class="abs svc card" style="left:450px">
  <svg class="icon" viewBox="0 0 60 60" fill="none" stroke="#222629" stroke-width="2"><rect x="10" y="12" width="40" height="28" rx="2"/><path d="M24 48h12M30 40v8M20 28l6-6 6 6 8-8"/></svg>
  <h3>Digital<br>Transformation</h3>
  <p>Process Automation via RPA and Conversational AI<br><br>Enterprise Application Integration</p>
  <span class="btn tag">View More</span>
</div>
<div class="abs svc" style="left:780px">
  <svg class="icon" viewBox="0 0 60 60" fill="none" stroke="#222629" stroke-width="2"><circle cx="30" cy="14" r="6"/><circle cx="14" cy="44" r="6"/><circle cx="46" cy="44" r="6"/><path d="M30 20v10M30 30L16 38M30 30l14 8"/></svg>
  <h3>Network<br>of Expertise</h3>
  <p>Full-stack development<br><br>From AI/ML and Beta to legacy</p>
</div>

<div class="abs solutions-band"></div>
<h2 class="abs section-title solutions-title"><span class="chev">›</span>OUR SOLUTIONS</h2>
<p class="abs solutions-text">Since the development and deployment of tmPilot in 2017, we have earned an impeccable track record with all of our clients. We have been able to satisfy all of their requirements and provide on-going support throughout the implementation journey. These requirements include, but are not limited to, multilingual capabilities, back-end integration competencies, and cybersecurity standards.</p>
<span class="abs btn tag solutions-btn">View More</span>
<div class="abs solutions-photo" role="img" aria-label="Businesswoman in glasses and a dark blazer pointing with a pen"></div>

<svg class="abs omni" viewBox="0 0 1200 700" preserveAspectRatio="none" aria-hidden="true">
  <defs><linearGradient id="wave" x1="0" y1="0" x2="0" y2="1"><stop offset="0" stop-color="#8acb55"/><stop offset="1" stop-color="#5fa12c"/></linearGradient></defs>
  <path d="M0 90 C300 0 560 40 760 110 C920 170 1080 140 1200 80 L1200 700 L0 700 Z" fill="url(#wave)"/>
  <path d="M0 200 C260 120 520 160 760 230 C920 280 1080 250 1200 200" stroke="rgba(255,255,255,.25)" stroke-width="2" fill="none"/>
</svg>
<div class="abs robot" role="img" aria-label="White humanoid robot pointing forward"></div>

<section class="abs request-box">
  <h2 class="section-title"><span class="chev">›</span>REQUEST US</h2>
  <div class="fields">
    <div class="field"><label>Name<b>*</b></label><div class="input"></div></div>
    <div class="field"><label>Phone<b>*</b></label><div class="input"></div></div>
    <div class="field"><label>Email<b>*</b></label><div class="input"></div></div>
    <div></div>
    <div class="field wide"><label>Your Message</label><div class="area">Type your message here...</div></div>
  </div>
  <span class="btn">Submit</span>
</section>

<h2 class="abs omni-title">Omni-language support</h2>
<p class="abs omni-text">tmPilot supports all written languages as long as they can be typed on a computer. While traditional AI chatbots require a "base language" or nothing in one language at a time, tmPilot works seamlessly in multilingual and mixed language environments.</p>
<span class="abs btn tag omni-btn">Explore</span>
<div class="abs product-name"><i></i>tmPilot</div>

<span class="abs arrow" style="left:80px;top:4395px">‹</span>
<div class="abs clients-row"><span>Lumen North</span><span>Paysora</span><span>Roadwise</span><span>Kestrel</span></div>
<span class="abs arrow" style="right:80px;top:4395px">›</span>

<footer class="abs footer">
  <div class="abs logo"><span class="mark"></span>VELBRIC</div>
  <div class="abs contact">Phone: (555) 014-2290<br>Email: info@velbriclimited.example<br>Address: 2800 Fieldline Avenue,<br>Unit 12 &amp; 14 Brookside, ON<br>Canada, L0A 0A0</div>
  <div class="abs fcol" style="left:470px"><h4>Menu</h4>Home<br>About Us<br>Services<br>Solutions<br>Contact Us</div>
  <div class="abs fcol" style="left:670px"><h4>Useful Links</h4>Careers<br>Supports<br>Terms &amp; Conditions<br>Privacy Policy</div>
  <div class="abs fcol news" style="left:880px"><h4>Newsletter</h4><div class="input">Enter your E-mail</div><span class="btn">Subscribe</span></div>
</footer>
<div class="abs bottombar">
  <div class="abs copy">© 2020 Velbric Limited. All rights reserved.</div>
  <div class="abs social"><i></i><i></i><i></i><i></i></div>
</div>

</body>
</html>
```